Cool modern, tech Business card design

Looking for a new business card design for our Managed IT Services company. We would like 2 sides, with the logo one one side horizontally and then the information on the back in either vertical or horizontal. We want our colors from the logo incorporated but also would like to see the color gray in there as well.

Target Market(s)

IT, Information Technology, Tech, Service

Industry/Entity Type

It Service

Contact Information for Business Card

Carl Penner
Managing Partner
(P)555-271-4830 ext xxx
(F)555-271-4831
www.brixtelcore.com

Font styles to use
Sans Serif

Colors
959595
000000
ec1f27

Requirements
Must have
• Logo on one side with some nice design or pattern
• Information on back in either vertical or horizontal format
Nice to have
• For it to look cool, tech, modern, stand out.

```html
<!DOCTYPE html>
<html lang="en">
<head>
<meta charset="utf-8">
<title>Brixtelcore Business Card</title>
<link rel="stylesheet" href="https://fonts.googleapis.com/css2?family=Fira+Sans:wght@400;500&display=swap">
<style>
  :root {
    --card-black: #000000;
    --brand-red: #ec1f27;
    --brand-red-deep: #a5121a;
    --brand-gray: #959595;
    --ink-white: #f2f2f2;
    --backdrop: #e3e4e8;
  }
  html, body {
    margin: 0;
    padding: 0;
    width: 1200px;
    height: 1200px;
    overflow: hidden;
    background: var(--backdrop);
    font-family: "Fira Sans", Arial, sans-serif;
  }
  .sheet {
    width: 1200px;
    height: 1200px;
    display: flex;
    flex-direction: column;
    align-items: center;
    justify-content: center;
    gap: 44px;
  }
  .card {
    position: relative;
    width: 900px;
    height: 514px;
    background: var(--card-black);
    overflow: hidden;
    box-shadow: 0 10px 30px rgba(0,0,0,0.25);
  }
  .card__edge-band {
    position: absolute;
    left: 0;
    top: 0;
    width: 34px;
    height: 100%;
    background: linear-gradient(90deg, var(--brand-red-deep), var(--brand-red) 60%);
  }
  .card__pattern {
    position: absolute;
    right: 0;
    top: 0;
    width: 560px;
    height: 100%;
    background:
      radial-gradient(ellipse 38% 30% at 68% 28%, rgba(149,149,149,0.22), rgba(0,0,0,0) 100%),
      radial-gradient(ellipse 34% 28% at 82% 72%, rgba(149,149,149,0.18), rgba(0,0,0,0) 100%),
      radial-gradient(ellipse 30% 24% at 40% 80%, rgba(149,149,149,0.12), rgba(0,0,0,0) 100%);
  }
  .card__pattern--corner {
    left: 34px;
    right: auto;
    width: 300px;
    height: 240px;
    background: radial-gradient(ellipse 60% 55% at 30% 25%, rgba(149,149,149,0.14), rgba(0,0,0,0) 100%);
  }
  .brand {
    color: var(--brand-gray);
    font-weight: 500;
    letter-spacing: 0.5px;
    white-space: nowrap;
  }
  .card--front .brand {
    position: absolute;
    left: 50%;
    top: 50%;
    transform: translate(-46%, -50%);
    font-size: 84px;
  }
  .card--back .brand {
    position: absolute;
    left: 90px;
    top: 50%;
    transform: translateY(-50%);
    font-size: 46px;
  }
  .card__divider {
    position: absolute;
    left: 470px;
    top: 150px;
    width: 2px;
    height: 214px;
    background: var(--brand-red);
  }
  .contact {
    position: absolute;
    left: 510px;
    top: 50%;
    transform: translateY(-50%);
    color: var(--ink-white);
    font-size: 24px;
    line-height: 1.45;
  }
  .contact__name {
    font-size: 38px;
    font-weight: 500;
    margin: 0 0 2px;
  }
  .contact__title,
  .contact__label,
  .contact__web {
    color: var(--brand-red);
  }
  .contact p { margin: 0; }
</style>
</head>
<body>
<main class="sheet">
  <section class="card card--front">
    <div class="card__edge-band"></div>
    <div class="card__pattern" role="img" aria-label="Faint gray network pattern decoration"></div>
    <div class="brand">brixtelcore</div>
  </section>

  <section class="card card--back">
    <div class="card__edge-band"></div>
    <div class="card__pattern card__pattern--corner" role="img" aria-label="Faint gray network pattern decoration"></div>
    <div class="brand">brixtelcore</div>
    <div class="card__divider"></div>
    <div class="contact">
      <p class="contact__name">Carl Penner</p>
      <p class="contact__title">Managing Partner</p>
      <p><span class="contact__label">(P)</span> 555-271-4830</p>
      <p><span class="contact__label">(F)</span> 555-271-4831</p>
      <p class="contact__web">www.brixtelcore.com</p>
    </div>
  </section>
</main>
</body>
</html>
```